Bright LumaTrex & Equipments

I need to create full stationery design for the company; Business Card, Envelop, Letterheads, Calendar and email template.

Our company is specialized in the import and export of nutritional, pharmaceutical and cosmetics in addition to medical equipments.

These is no limitation on how to use colors within the design.

Target Market(s)

Global

Industry/Entity Type

Healthcare

Other font styles liked:
• a font close to logo. Letterhead body text to be different than the address text

Requirements
Nice to have
• We will have multiple locations so it is good to keep space for future addresses.
• Stationary requirements:
• Letterhead: A4
• Envelopes: 3 regular sizes : large, medium and small (i do not know the sizes)
• Colors: extracted from the logo

```html
<!DOCTYPE html>
<html lang="en">
<head>
<meta charset="utf-8">
<title>Bright LumaTrex &amp; Equipments – Business Card</title>
<link href="https://fonts.googleapis.com/css2?family=Arimo:wght@400;700&display=swap" rel="stylesheet">
<style>
  :root {
    --navy: #0b0f5e;
    --navy-deep: #070a44;
    --cyan: #2aa7df;
    --green: #3aa935;
    --ink: #4a4a4a;
    --white: #ffffff;
    --backdrop: #e8e5df;
  }
  * { box-sizing: border-box; margin: 0; padding: 0; }
  html, body {
    width: 1200px; height: 950px; overflow: hidden;
    background: var(--backdrop);
    font-family: "Arimo", Arial, sans-serif;
  }
  .card {
    position: absolute; left: 220px;
    width: 760px; height: 434px;
    border-radius: 22px; overflow: hidden;
    box-shadow: 0 6px 18px rgba(0,0,0,.18);
  }
  .card--front { top: 30px; background: var(--white); }
  .card--back {
    top: 486px;
    background: linear-gradient(135deg, var(--navy) 0%, var(--navy-deep) 100%);
    display: flex; flex-direction: column; align-items: center; justify-content: center; gap: 18px;
  }

  .brand { position: absolute; left: 44px; top: 44px; display: flex; align-items: center; gap: 14px; }
  .brand__mark { width: 36px; height: 36px; background: var(--cyan); }
  .brand__name { font-weight: 700; font-size: 29px; color: var(--cyan); letter-spacing: -.2px; }

  .band { position: absolute; inset: 0; }

  .contact {
    position: absolute; left: 50px; top: 214px;
    color: var(--white); font-size: 19px; line-height: 29px;
    list-style: none;
  }
  .contact__row { display: flex; align-items: center; gap: 10px; }
  .contact__row--plain { padding-left: 30px; }
  .contact__icon { width: 20px; height: 20px; flex: none; }

  .person { position: absolute; right: 44px; top: 118px; text-align: right; }
  .person__name { font-weight: 700; font-size: 27px; color: var(--cyan); }
  .person__title { font-size: 20px; color: var(--green); margin-top: 4px; }
  .person__email { font-size: 19px; color: var(--ink); margin-top: 4px; }

  .back-brand { display: flex; align-items: center; gap: 16px; }
  .back-brand__mark { width: 44px; height: 44px; background: var(--white); }
  .back-brand__name { font-weight: 700; font-size: 34px; color: var(--white); }
  .back-web { font-size: 18px; letter-spacing: 4px; color: rgba(255,255,255,.75); }
</style>
</head>
<body>

<section class="card card--front">
  <svg class="band" viewBox="0 0 760 434" preserveAspectRatio="none" aria-hidden="true">
    <polygon points="0,196 760,238 760,434 0,434" fill="var(--navy)"/>
  </svg>

  <div class="brand">
    <span class="brand__mark"></span>
    <span class="brand__name">Bright LumaTrex &amp; Equipments</span>
  </div>

  <ul class="contact">
    <li class="contact__row contact__row--plain">4120 Cedar Hollow Road</li>
    <li class="contact__row">
      <svg class="contact__icon" viewBox="0 0 20 20"><path d="M4 3h4l1.5 4-2 1.5a10 10 0 0 0 4 4L13 10.5l4 1.5v4a2 2 0 0 1-2 2A14 14 0 0 1 2 5a2 2 0 0 1 2-2z" fill="var(--white)"/></svg>
      <span>Northvale, Alaska 34120</span>
    </li>
    <li class="contact__row">
      <svg class="contact__icon" viewBox="0 0 20 20"><rect x="5" y="2" width="10" height="5" fill="var(--white)"/><rect x="2" y="8" width="16" height="7" rx="1.5" fill="var(--white)"/><rect x="5" y="13" width="10" height="5" fill="var(--white)" stroke="var(--navy)" stroke-width="1"/></svg>
      <span>555 0142 7781</span>
    </li>
    <li class="contact__row">
      <svg class="contact__icon" viewBox="0 0 20 20"><path d="M4 3h4l1.5 4-2 1.5a10 10 0 0 0 4 4L13 10.5l4 1.5v4a2 2 0 0 1-2 2A14 14 0 0 1 2 5a2 2 0 0 1 2-2z" fill="var(--white)"/></svg>
      <span>555 0198 3364</span>
    </li>
    <li class="contact__row">
      <svg class="contact__icon" viewBox="0 0 20 20"><circle cx="10" cy="10" r="8" fill="none" stroke="var(--white)" stroke-width="2"/><ellipse cx="10" cy="10" rx="3.5" ry="8" fill="none" stroke="var(--white)" stroke-width="1.5"/><line x1="2" y1="10" x2="18" y2="10" stroke="var(--white)" stroke-width="1.5"/></svg>
      <span>www.brightluma.example</span>
    </li>
  </ul>

  <div class="person">
    <p class="person__name">Marcus Hale</p>
    <p class="person__title">President</p>
    <p class="person__email">marcus@brightluma.example</p>
  </div>
</section>

<section class="card card--back">
  <div class="back-brand">
    <span class="back-brand__mark"></span>
    <span class="back-brand__name">Bright LumaTrex &amp; Equipments</span>
  </div>
  <p class="back-web">www.brightluma.example</p>
</section>

</body>
</html>
```